Brochure Annual Report Design

I want to create a brochure / annual report for our company. Can you help me. I like this design. https://pixelstallhub.com/Brightfold/2847163-Annual-Report-2018. Here is our company website www.velmordental.com. Please take the logo from there. Our website needs an upgrade in how it looks. I would like the brochure annual report and the website to look somewhat congruent. I also want to create a very high end magazine that is fun for our company eventually.

We are a company that helps dentists create better practices by really improving the way they do business and motivating their teams. As a result they have more fun, more profit, happier team members, and they all have better lives.

Target Market(s)

dentist

Industry/Entity Type

Dental

Number of Pages Required

5+ page

Colors
0255a3
85cae6
ffffff

Requirements
Must have
• Must look really good.
Nice to have
• Any creative suggestions are welcomed. I need a website that looks congruent to the brochure and annual report. I also want to create a very high end magazine that is fun for our company eventually.
Should not have
• I don't like low quality design.

```html
<!DOCTYPE html>
<html lang="en">
<head>
<meta charset="utf-8">
<title>Velmor Dental — Annual Report 2018</title>
<link rel="stylesheet" href="https://fonts.googleapis.com/css2?family=Open+Sans:wght@400;600;700;800&display=swap">
<style>
  :root{
    --navy:#0f2f66;
    --blue:#0255a3;
    --sky:#85cae6;
    --sky-pale:#d6edf7;
    --white:#ffffff;
    --paper:#f5f6f7;
    --gray:#7b7f84;
    --gray-dark:#4a4e54;
    --rule:#c9d3dc;
    --backdrop:#e7edf2;
  }
  *{box-sizing:border-box;margin:0;padding:0}
  html,body{width:870px;height:1200px;overflow:hidden}
  body{background:var(--backdrop);font-family:"Open Sans",Arial,sans-serif;color:var(--gray-dark);position:relative}

  .spread{position:absolute;left:55px;width:760px;height:538px;display:flex;box-shadow:0 6px 18px rgba(15,47,102,.18)}
  .spread--cover{top:30px}
  .spread--inside{top:630px}
  .page{position:relative;width:380px;height:538px;background:var(--white);overflow:hidden}
  .page--inside{background:var(--paper)}
  .page svg.shapes{position:absolute;inset:0;width:100%;height:100%}

  /* wordmark */
  .wordmark{display:flex;align-items:center;gap:5px;font-weight:700;color:var(--blue);font-size:13px;letter-spacing:.2px}
  .wordmark__dot{width:8px;height:8px;background:var(--sky)}
  .wordmark--light{color:var(--white);font-size:22px}
  .wordmark--light .wordmark__dot{width:12px;height:12px}

  /* back cover */
  .contact{position:absolute;left:28px;top:28px;width:170px}
  .contact__phone{margin-top:6px;font-size:11px;font-weight:700;color:var(--blue)}
  .contact__address{font-size:8px;line-height:1.45;color:var(--gray);margin-top:2px}
  .contact__web{font-size:8px;color:var(--sky);margin-top:3px;padding-bottom:5px;border-bottom:1.5px solid var(--sky)}
  .photo{position:absolute;left:0;top:185px;width:318px;height:195px;background:linear-gradient(120deg,#6b4a3a 0%,#a7775d 45%,#d9c7b8 70%,#8c5a48 100%)}

  /* front cover */
  .cover-mark{position:absolute;right:34px;top:196px}
  .cover-title{position:absolute;right:30px;bottom:62px;text-align:right;line-height:.95}
  .cover-title__line1{font-size:40px;font-weight:800;color:var(--navy)}
  .cover-title__line2{font-size:40px;font-weight:800;color:var(--sky)}
  .cover-web{position:absolute;right:30px;bottom:30px;background:var(--sky);color:var(--white);font-size:11px;font-weight:600;padding:4px 14px}

  /* inside pages */
  .inside-mark{position:absolute;top:24px}
  .page--left .inside-mark{left:28px}
  .page--right .inside-mark{right:28px}
  .section-title{position:absolute;left:28px;top:54px;border-left:3px solid var(--blue);padding-left:7px;line-height:1}
  .section-title__main{font-size:24px;font-weight:800;color:var(--sky)}
  .section-title__sub{font-size:14px;font-weight:700;color:var(--gray)}
  .stats{position:absolute;left:28px;top:112px;display:flex;gap:8px}
  .stat{width:102px;height:64px;color:var(--white);padding:8px 9px}
  .stat--sky{background:var(--sky)}
  .stat--gray{background:var(--gray);margin-top:10px}
  .stat--blue{background:var(--blue);margin-top:20px}
  .stat__label{font-size:7px;font-weight:700;letter-spacing:.4px}
  .stat__value{font-size:15px;font-weight:800;margin-top:6px}

  .table-grid{position:absolute;left:28px;right:28px;display:grid;grid-template-columns:1fr 1fr;gap:14px 16px}
  .page--left .table-grid{top:212px}
  .fin-table{width:100%;border-collapse:collapse;font-size:6.5px}
  .fin-table caption{text-align:left;font-size:7.5px;font-weight:700;color:var(--blue);padding-bottom:3px;border-bottom:1.5px solid var(--blue)}
  .fin-table th{color:var(--sky);font-weight:700;text-align:right;padding:3px 2px}
  .fin-table th:first-child,.fin-table td:first-child{text-align:left}
  .fin-table td{padding:3px 2px;border-bottom:.5px solid var(--rule);text-align:right}
  .fin-table tr.total td{color:var(--blue);font-weight:700;border-bottom:none}
  .fin-table td.shade{background:#e3e7eb}

  .wide-table{position:absolute;left:28px;right:28px}
  .wide-table--top{top:62px}
  .wide-table--bottom{top:330px}
  .article{position:absolute;left:28px;right:28px;top:238px}
  .article__head{font-size:10px;font-weight:800;color:var(--blue);margin-bottom:5px}
  .article__body{font-size:6.8px;line-height:1.55;color:var(--gray)}
  .folio{position:absolute;bottom:16px;font-size:7px;color:var(--gray)}
  .page--left .folio{left:28px}
  .page--right .folio{right:28px}
  .page--left.page--inside::after{content:"";position:absolute;right:0;top:0;width:14px;height:100%;background:linear-gradient(90deg,transparent,rgba(0,0,0,.07))}
  .page--right.page--inside::before{content:"";position:absolute;left:0;top:0;width:14px;height:100%;background:linear-gradient(270deg,transparent,rgba(0,0,0,.07))}
</style>
</head>
<body>

<!-- Cover spread: back cover + front cover -->
<section class="spread spread--cover" aria-label="Cover">
  <div class="page page--back">
    <svg class="shapes" viewBox="0 0 380 538" aria-hidden="true">
      <rect x="0" y="150" width="380" height="35" fill="var(--sky)"/>
      <polygon points="318,185 380,150 380,380 318,380" fill="var(--blue)"/>
      <rect x="0" y="380" width="380" height="18" fill="#eef1f4"/>
    </svg>
    <div class="photo" role="img" aria-label="Photo of a presenter with a microphone speaking to a seated audience"></div>
    <div class="contact">
      <div class="wordmark"><span class="wordmark__dot"></span>Velmor Dental</div>
      <p class="contact__phone">800.555.0142</p>
      <p class="contact__address">4410 W 118th Street<br>Suite 210<br>Lakeview Park, KS 66099</p>
      <p class="contact__web">www.velmordental.com</p>
    </div>
  </div>

  <div class="page page--front">
    <svg class="shapes" viewBox="0 0 380 538" aria-hidden="true">
      <rect x="0" y="0" width="380" height="538" fill="#f3f5f7"/>
      <polygon points="0,150 380,110 380,320 0,380" fill="var(--navy)"/>
      <polygon points="0,380 380,320 380,336 0,398" fill="var(--white)"/>
      <polygon points="0,398 380,336 380,372 0,432" fill="var(--blue)"/>
      <polygon points="0,150 60,150 0,185" fill="var(--sky)"/>
    </svg>
    <div class="cover-mark wordmark wordmark--light"><span class="wordmark__dot"></span>Velmor Dental</div>
    <h1 class="cover-title"><span class="cover-title__line1">ANNUAL</span><br><span class="cover-title__line2">REPORT 2018</span></h1>
    <p class="cover-web">www.velmordental.com</p>
  </div>
</section>

<!-- Inside spread: financial report -->
<section class="spread spread--inside" aria-label="Financial report">
  <div class="page page--left page--inside">
    <div class="inside-mark wordmark"><span class="wordmark__dot"></span>Velmor Dental</div>
    <h2 class="section-title"><span class="section-title__main">FINANCIAL</span><br><span class="section-title__sub">REPORT</span></h2>
    <div class="stats">
      <div class="stat stat--sky"><p class="stat__label">THE MARKETS</p><p class="stat__value">$321,789</p></div>
      <div class="stat stat--gray"><p class="stat__label">NET SALES</p><p class="stat__value">+$44,178</p></div>
      <div class="stat stat--blue"><p class="stat__label">GLOBAL MARKET</p><p class="stat__value">$102,098</p></div>
    </div>
    <div class="table-grid">
      <table class="fin-table">
        <caption>Revenue Sources</caption>
        <tr><th>Item</th><th>2017</th><th>2018</th></tr>
        <tr><td>Coaching programs</td><td>$84,210</td><td>$96,480</td></tr>
        <tr><td>Team workshops</td><td>$52,300</td><td>$61,950</td></tr>
        <tr><td>Practice audits</td><td>$31,120</td><td>$38,400</td></tr>
        <tr><td>Online courses</td><td>$18,640</td><td>$22,310</td></tr>
        <tr class="total"><td>Total</td><td>$186,270</td><td>$219,140</td></tr>
      </table>
      <table class="fin-table">
        <caption>Operating Costs</caption>
        <tr><th>Item</th><th>2017</th><th>2018</th></tr>
        <tr><td>Staff</td><td>$61,400</td><td>$66,900</td></tr>
        <tr><td>Travel</td><td>$14,250</td><td>$15,780</td></tr>
        <tr><td>Events</td><td>$22,100</td><td>$24,630</td></tr>
        <tr><td>Software</td><td>$6,320</td><td>$7,050</td></tr>
        <tr class="total"><td>Total</td><td>$104,070</td><td>$114,360</td></tr>
      </table>
      <table class="fin-table">
        <caption>Client Growth</caption>
        <tr><th>Item</th><th>2017</th><th>2018</th></tr>
        <tr><td>New practices</td><td>42</td><td>57</td></tr>
        <tr><td>Renewals</td><td>118</td><td>131</td></tr>
        <tr><td>Referrals</td><td>36</td><td>49</td></tr>
        <tr class="total"><td>Total</td><td>196</td><td>237</td></tr>
      </table>
      <table class="fin-table">
        <caption>Team Results</caption>
        <tr><th>Item</th><th>2017</th><th>2018</th></tr>
        <tr><td>Retention</td><td>88%</td><td>92%</td></tr>
        <tr><td>Satisfaction</td><td>4.5</td><td>4.7</td></tr>
        <tr><td>Profit lift</td><td>14%</td><td>19%</td></tr>
        <tr class="total"><td>Average</td><td>—</td><td>+6%</td></tr>
      </table>
    </div>
    <p class="folio">24</p>
  </div>

  <div class="page page--right page--inside">
    <div class="inside-mark wordmark"><span class="wordmark__dot"></span>Velmor Dental</div>
    <table class="fin-table wide-table wide-table--top">
      <caption>Net Sales by Region</caption>
      <tr><th>Region</th><th>2017</th><th>2018</th><th>Change</th></tr>
      <tr><td>Midwest</td><td class="shade">$54,120</td><td>$61,480</td><td>13.6%</td></tr>
      <tr><td>Northeast</td><td class="shade">$38,900</td><td>$42,310</td><td>8.8%</td></tr>
      <tr><td>South</td><td class="shade">$33,760</td><td>$39,050</td><td>15.7%</td></tr>
      <tr><td>West</td><td class="shade">$29,410</td><td>$34,200</td><td>16.3%</td></tr>
      <tr><td>Canada</td><td class="shade">$12,080</td><td>$14,960</td><td>23.8%</td></tr>
      <tr class="total"><td>Total</td><td class="shade">$168,270</td><td>$192,000</td><td>14.1%</td></tr>
    </table>
    <div class="article">
      <h3 class="article__head">RIT, CUS ALIQUI DENTIUM NECEATUS.</h3>
      <p class="article__body">Our coaching work grew steadily this year as more practices joined the program. Teams reported higher morale, stronger patient care and better profit. We invested in new workshops, online courses and regional events, and we expect this growth to continue through the coming year.</p>
    </div>
    <table class="fin-table wide-table wide-table--bottom">
      <caption>Key Indicators</caption>
      <tr><th>Indicator</th><th>Value</th><th>Change</th></tr>
      <tr><td>Gross margin</td><td class="shade">48.2%</td><td>+3.1%</td></tr>
      <tr><td>Net margin</td><td class="shade">21.6%</td><td>+2.4%</td></tr>
      <tr><td>Cash flow</td><td class="shade">$58,740</td><td>+9.2%</td></tr>
      <tr><td>Debt ratio</td><td class="shade">0.18</td><td>−0.04</td></tr>
      <tr class="total"><td>Overall</td><td class="shade">Strong</td><td>+5.7%</td></tr>
    </table>
    <p class="folio">25</p>
  </div>
</section>

</body>
</html>
```